Create a wine label for our soon to be released Sparkling Wine

As we are about to release our new Sparkling Wine we are in need of a new label. Dimensions and text as per attached file, the design is more or less free style, but keep it a classic sparkling wine label. Keep it clean. Bottle will be near to black with black/silver cap You can use Script Font. No green, red or gold colours. We like black and silver, but don't be afraid to use some color somewhere (we can always change that). We thought of printing our logo in silver foil so a black label would be nice.

Target Market(s)

wine industry

Font styles to use
Script
Other font styles liked:
• GaramITC

Requirements
Must have
• Dimensions and text as per attached file
Nice to have
• Classic wine label
Should not have
• No gold or red or green colour

```html
<!DOCTYPE html>
<html lang="en">
<head>
<meta charset="utf-8">
<title>Frost Hollow – Blanc de Noir Label</title>
<link href="https://fonts.googleapis.com/css2?family=Cinzel:wght@400;600&family=Pinyon+Script&display=swap" rel="stylesheet">
<style>
  :root {
    --backdrop: #e9e9e6;
    --label-edge: #f4f4f4;
    --frame-silver: #9a9a9a;
    --frame-light: #d0d0d0;
    --stripe-dark: #161616;
    --stripe-mid: #262626;
    --title-white: #f2f2f2;
    --region-grey: #8a8a8a;
    --varietal-ice: #a8cbe6;
    --detail-grey: #d6d6d6;
    --mark-silver: #bdbdbd;
  }
  * { margin: 0; padding: 0; box-sizing: border-box; }
  html, body {
    width: 1200px; height: 800px; overflow: hidden;
    background: var(--backdrop);
  }
  .canvas {
    position: relative; width: 1200px; height: 800px;
  }
  .label {
    position: absolute; left: 275px; top: 75px;
    width: 650px; height: 650px;
    background: var(--label-edge);
    box-shadow: 0 2px 10px rgba(0,0,0,0.12);
  }
  .label-frame {
    position: absolute; inset: 0; width: 650px; height: 650px;
  }
  .label-content {
    position: absolute; inset: 0;
    text-align: center;
    font-family: "Cinzel", Georgia, serif;
  }
  .brand-title {
    position: absolute; left: 0; right: 0; top: 98px;
    font-size: 44px; font-weight: 400; letter-spacing: 1px; line-height: 70px;
    color: var(--title-white);
  }
  .brand-title .cap { font-size: 60px; }
  .region {
    position: absolute; left: 0; right: 0; top: 182px;
    font-family: "Pinyon Script", cursive;
    font-size: 30px; line-height: 40px; color: var(--region-grey);
  }
  .brand-mark {
    position: absolute; left: 0; right: 0; top: 318px;
    display: flex; justify-content: center; align-items: center; gap: 14px;
  }
  .brand-mark-square {
    width: 26px; height: 26px; background: var(--mark-silver);
  }
  .brand-mark-name {
    font-size: 28px; font-weight: 400; line-height: 36px; color: var(--mark-silver);
    letter-spacing: 1px;
  }
  .varietal {
    position: absolute; left: 0; right: 0; top: 460px;
    font-size: 36px; font-weight: 600; line-height: 50px; color: var(--varietal-ice);
  }
  .varietal .cap { font-size: 44px; }
  .details {
    position: absolute; left: 0; right: 0; top: 514px;
    display: grid; grid-template-columns: 318px 1fr; column-gap: 10px;
    font-size: 17px; line-height: 24px; color: var(--detail-grey);
  }
  .details .key { text-align: right; }
  .details .value { text-align: left; }
</style>
</head>
<body>
<main class="canvas">
  <section class="label">
    <svg class="label-frame" viewBox="0 0 650 650" aria-hidden="true">
      <defs>
        <pattern id="pinstripe" width="9" height="9" patternUnits="userSpaceOnUse">
          <rect width="9" height="9" fill="var(--stripe-dark)"/>
          <rect width="4" height="9" fill="var(--stripe-mid)"/>
        </pattern>
      </defs>
      <path d="M36 12 H614 A24 24 0 0 0 638 36 V614 A24 24 0 0 0 614 638 H36 A24 24 0 0 0 12 614 V36 A24 24 0 0 0 36 12 Z" fill="var(--frame-silver)"/>
      <path d="M40 20 H610 A20 20 0 0 0 630 40 V610 A20 20 0 0 0 610 630 H40 A20 20 0 0 0 20 610 V40 A20 20 0 0 0 40 20 Z" fill="url(#pinstripe)"/>
      <path d="M44 28 H606 A16 16 0 0 0 622 44 V606 A16 16 0 0 0 606 622 H44 A16 16 0 0 0 28 606 V44 A16 16 0 0 0 44 28 Z" fill="none" stroke="var(--frame-light)" stroke-width="1.5"/>
    </svg>
    <div class="label-content">
      <h1 class="brand-title"><span class="cap">F</span>ROST <span class="cap">H</span>OLLOW</h1>
      <p class="region">Tasmania</p>
      <div class="brand-mark">
        <span class="brand-mark-square"></span>
        <span class="brand-mark-name">FROST HOLLOW</span>
      </div>
      <h2 class="varietal"><span class="cap">B</span>LANC DE <span class="cap">N</span>OIR</h2>
      <dl class="details">
        <dt class="key">Product of Australia</dt><dd class="value">2013</dd>
        <dt class="key">750mL</dt><dd class="value">Vintage Sparkling</dd>
        <dt class="key">Alc/Vol 12.5%</dt><dd class="value">Méthode Traditionnelle</dd>
      </dl>
    </div>
  </section>
</main>
</body>
</html>
```